Promotional Poster for "Bowls & Barrels" Community Event

Bowls & Barrels is a fun, high-energy annual fundraising event where guests enjoy gourmet taco creations and craft beer from some of Clark County's finest chefs and brewers. This community event is a fundraiser, supporting Hollis Ridge Food Bank in Southwest Washington. We need a 11x17" full-color event poster for our 2019 Bowls & Barrels event. For more information, visit our event website: www.bowlsandbarrels-fest.org
Target Market(s)
Poster to be displayed in breweries, restaurants, bars, and taprooms
Industry/Entity Type
Non Profit
Colors
Designer to choose colors to be used in the design.
Look and feel
Each slider illustrates characteristics of the customer's brand and the style your logo design should communicate.

```html
<!DOCTYPE html>
<html lang="en">
<head>
<meta charset="utf-8">
<title>Bowls &amp; Barrels 2019</title>
<link rel="stylesheet" href="https://fonts.googleapis.com/css2?family=Bungee&family=Russo+One&family=Open+Sans:wght@600&family=Audiowide&display=swap">
<style>
  :root {
    --bg: #05040a;
    --white: #ffffff;
    --date-orange: #ff8a3c;
    --date-glow: #ff3d8b;
    --price-yellow: #f6e62b;
    --price-cyan: #3fd8f2;
    --web-green: #53e07a;
    --badge-pink: #e8196f;
    --star-gold: #e6b23a;
    --ball-light: #d9f1ff;
    --ball-mid: #7aa8ff;
    --ball-deep: #b04fe0;
  }
  * { margin: 0; padding: 0; box-sizing: border-box; }
  html, body { width: 764px; height: 1200px; overflow: hidden; background: var(--bg); }
  .poster {
    position: relative;
    width: 764px;
    height: 1200px;
    overflow: hidden;
    background:
      radial-gradient(ellipse at 50% 30%, rgba(90,70,200,0.25), transparent 60%),
      var(--bg);
    color: var(--white);
  }
  .light-streaks {
    position: absolute;
    inset: 0;
    background:
      radial-gradient(ellipse 340px 60px at 75% 52%, rgba(255,60,180,0.35), transparent 70%),
      radial-gradient(ellipse 300px 50px at 20% 40%, rgba(60,160,255,0.3), transparent 70%),
      radial-gradient(ellipse 200px 40px at 85% 22%, rgba(80,230,120,0.25), transparent 70%);
  }
  .partner-name {
    position: absolute;
    left: 26px;
    top: 44px;
    display: flex;
    align-items: center;
    gap: 12px;
    font-family: "Open Sans", sans-serif;
    font-weight: 600;
    font-size: 20px;
    line-height: 1.05;
    letter-spacing: 0.5px;
    text-transform: uppercase;
  }
  .partner-name .mark {
    width: 40px; height: 40px;
    border-radius: 50%;
    background: var(--white);
  }
  .event-name {
    position: absolute;
    right: 40px;
    top: 30px;
    font-family: "Bungee", sans-serif;
    font-size: 34px;
    line-height: 1.05;
    text-align: center;
    color: var(--white);
  }
  .ball-string {
    position: absolute;
    left: 381px; top: 0;
    width: 2px; height: 140px;
    background: #888;
  }
  .disco-ball {
    position: absolute;
    left: 214px; top: 120px;
    width: 336px; height: 336px;
    border-radius: 50%;
    background: radial-gradient(circle at 38% 35%, var(--ball-light) 0%, var(--ball-mid) 45%, var(--ball-deep) 80%, #3a1a6a 100%);
    box-shadow: 0 0 60px rgba(120,160,255,0.45);
  }
  .dates {
    position: absolute;
    left: 0; right: 0;
    top: 462px;
    text-align: center;
    font-family: "Bungee", sans-serif;
    font-size: 42px;
    line-height: 1.1;
    color: var(--date-orange);
    text-shadow: 0 0 10px var(--date-glow), 0 0 3px var(--date-glow);
  }
  .pricing {
    position: absolute;
    left: 0; right: 0;
    top: 566px;
    text-align: center;
    font-family: "Russo One", sans-serif;
    font-size: 30px;
    line-height: 1.12;
  }
  .pricing .general { color: var(--price-yellow); }
  .pricing .vip { color: var(--white); }
  .pricing .packs { color: var(--price-cyan); }
  .highlights {
    position: absolute;
    left: 0; right: 0;
    top: 680px;
    text-align: center;
    font-family: "Open Sans", sans-serif;
    font-weight: 600;
    font-size: 19px;
    line-height: 1.35;
  }
  .website {
    position: absolute;
    left: 0; right: 0;
    top: 790px;
    text-align: center;
    font-family: "Audiowide", sans-serif;
    font-size: 24px;
    color: var(--web-green);
  }
  .age-badge {
    position: absolute;
    left: 680px; top: 762px;
    width: 74px; height: 74px;
    border-radius: 50%;
    background: var(--badge-pink);
    display: flex;
    align-items: center;
    justify-content: center;
    text-align: center;
    font-family: "Russo One", sans-serif;
    font-size: 13px;
    line-height: 1.1;
    color: var(--white);
  }
  .age-badge strong { font-size: 20px; display: block; }
  .corner-stars { position: absolute; left: 0; top: 700px; }
</style>
</head>
<body>
<main class="poster">
  <div class="light-streaks" role="img" aria-label="Coloured disco light streaks across a dark background"></div>

  <div class="partner-name"><span class="mark"></span><span>Hollis Ridge<br>Food Bank</span></div>
  <div class="event-name">Bowls<br>&amp; Barrels</div>

  <div class="ball-string"></div>
  <div class="disco-ball" role="img" aria-label="Glittering mirrored disco ball in blue, pink and purple tiles"></div>

  <h1 class="dates">FRIDAY, MAY 3, 2019<br>SATURDAY, MAY 4, 2019</h1>

  <div class="pricing">
    <p class="general">GENERAL ADMISSION: $35</p>
    <p class="vip">VIP FIESTA TICKET: $45</p>
    <p class="packs">6 PACK TICKETS AVAILABLE</p>
  </div>

  <div class="highlights">
    <p>Featuring:</p>
    <p>12 breweries &nbsp;-&nbsp; 12 restaurants</p>
    <p>Desserts &amp; beverages &nbsp;-&nbsp; Raffle drawing</p>
    <p>Live Music &nbsp;-&nbsp; Beer Bottle Ring Toss</p>
  </div>

  <p class="website">www.bowlsandbarrels-fest.org</p>

  <div class="age-badge"><span>MUST BE<strong>21+</strong></span></div>

  <svg class="corner-stars" width="160" height="180" viewBox="0 0 160 180" aria-hidden="true">
    <polygon points="40,20 58,70 110,72 68,102 84,152 40,122 -4,152 12,102 -30,72 22,70"
             fill="none" stroke="var(--star-gold)" stroke-width="4"/>
    <polygon points="48,110 56,132 80,133 61,147 68,170 48,156 28,170 35,147 16,133 40,132"
             fill="none" stroke="var(--star-gold)" stroke-width="3"/>
  </svg>
</main>
</body>
</html>
```